NEW Website DESIGN for Brightfold Panes & Worktops Company

Brand New website, contemporary, clean, visual (images), not busy. ATTACHED IS OUR LOG THAT YOU MUST USE.

The company is called Brightfold Panes & Worktops (BrightfoldPW)
www.brightfoldpw.com
The website should be www.brightfoldpnw.com
one page for glass one page for solid surfaces www.brightfoldpanesplashes.co.uk
www.brightfoldpanesworktops.co.uk

Target Market(s)

Hotels, Commercial projects, Small focus on residential

Industry/Entity Type

Construction

Number of Pages Required

5+ page

Font styles to use
Sans Serif

Requirements
Must have
• COLOURS AS PER OUR LOGO - WHITE/YELLOW/GREY - WHITE BACK GROUND
• CLEAR SIMPLE NAVIGATION - MODER CLEAN CUT - DESIGN FEEL
• LATEST NAVIGATION FOR IMAGES and text to include per project details
• WORK/PROJECT AREA - NEWS AREA - TEAM AREA/ABOUT US/CONTACT US
• NEW PAGEwww.brightfoldpanesplashes.co.uk - NEW PAGE www.brightfoldpanesworktops.co.uk
• PLEASE COPY THIS TYPE OF TEMPALTE
• https://www.velmarbuild.co.uk/project/grand-suites/
• MOBILE READY
• WORDPRESS
• MODERN IMAGES INCLUDING LUMERAX HALVERN AND GLASS PROJECTS
Nice to have
• NEW DESIGN MODER FRESH
• WEBSITES I LIKE THE TEMPLATE SHOULD BE LIKE THE WEBSITE BELOW
• https://www.velmarbuild.co.uk/
Should not have
• NOT Old fashion template, not busy NAVIGATION
• NO BLACK
• NO DARK GREYS
• NOT LOTS OF YELLOW
• RESDENTIAL IMAGES

```html
<!DOCTYPE html>
<html lang="en">
<head>
<meta charset="utf-8">
<title>Brightfold Panes &amp; Worktops</title>
<link rel="stylesheet" href="https://fonts.googleapis.com/css2?family=Roboto:wght@300;400;500;700;900&family=Open+Sans:wght@400;600&display=swap">
<style>
  :root {
    --yellow: #e4e11a;
    --white: #ffffff;
    --text: #3a3a3a;
    --text-soft: #6a6a6a;
    --line: #cfcfcf;
    --band: #ececec;
    --footer: #e0e0e0;
    --icon: #555555;
  }
  * { margin: 0; padding: 0; box-sizing: border-box; }
  html, body { width: 1200px; height: 2459px; overflow: hidden; background: var(--white); }
  body { position: relative; font-family: "Roboto", Arial, sans-serif; color: var(--text); }

  /* Hero */
  .hero { position: absolute; left: 0; top: 0; width: 1200px; height: 615px; overflow: hidden; }
  .hero-photo { position: absolute; inset: 0;
    background:
      radial-gradient(ellipse 260px 420px at 600px 520px, rgba(70,38,28,0.85), rgba(70,38,28,0) 100%),
      linear-gradient(90deg, #c9c3ba 0%, #b3aca3 22%, #8c837a 38%, #5a4e47 50%, #8f877f 62%, #bdb6ad 80%, #a59d94 100%);
  }
  .hero-photo::after { content: ""; position: absolute; inset: 0;
    background: linear-gradient(180deg, rgba(255,255,255,0.10) 0%, rgba(0,0,0,0) 40%, rgba(0,0,0,0.10) 100%); }
  .brand-box { position: absolute; left: 133px; top: 0; width: 215px; height: 148px; background: var(--white);
    display: flex; flex-direction: column; align-items: center; justify-content: center; gap: 12px; }
  .brand-dot { width: 56px; height: 56px; border-radius: 50%; background: var(--yellow); }
  .brand-name { font-size: 14.5px; font-weight: 500; color: #555; text-align: center; line-height: 1.2; }
  .main-nav { position: absolute; left: 348px; top: 0; width: 719px; height: 34px; background: var(--yellow);
    display: flex; justify-content: flex-end; align-items: center; gap: 32px; padding-right: 24px; }
  .main-nav a { font-size: 13px; color: #222; text-decoration: none; }
  .hero-title { position: absolute; left: 0; width: 1200px; top: 242px; text-align: center;
    color: var(--white); font-size: 40px; font-weight: 400; line-height: 48px; }
  .hero-btn { position: absolute; left: 544px; top: 354px; width: 110px; height: 43px; background: var(--yellow);
    color: #222; font-size: 16px; display: flex; align-items: center; justify-content: center; }
  .hero-arrow { position: absolute; top: 313px; }

  /* Welcome */
  .welcome-title { position: absolute; left: 133px; top: 712px; font-size: 50px; font-weight: 900; color: var(--yellow); }
  .welcome-text { position: absolute; left: 133px; top: 778px; width: 600px; font-size: 11.3px; line-height: 23.3px;
    color: var(--text); white-space: nowrap; }
  .welcome-media { position: absolute; left: 754px; top: 697px; width: 313px; height: 336px;
    background:
      linear-gradient(180deg, rgba(255,255,255,0.25) 0%, rgba(255,255,255,0) 50%),
      linear-gradient(90deg, #5fa89a 0%, #9fd0c5 30%, #d6ebe6 55%, #b7d9d1 75%, #e8f2ef 100%); }

  /* Projects */
  .section-title { position: absolute; left: 0; width: 1200px; text-align: center; font-size: 48px; font-weight: 900; color: var(--yellow); }
  .slider-btn { position: absolute; top: 1124px; width: 22px; height: 22px; border: 1px solid #888; background: var(--white); }
  .project-tile { position: absolute; width: 400px; }
  .project-card { position: absolute; left: 400px; top: 1479px; width: 400px; height: 303px;
    background: linear-gradient(135deg, #faf9f7 0%, #f1efeb 100%); text-align: center; }
  .project-card h3 { font-size: 24px; font-weight: 400; color: #222; margin-top: 50px; }
  .project-card p { font-family: "Open Sans", Arial, sans-serif; font-size: 10.8px; line-height: 20.5px;
    color: var(--text-soft); width: 340px; margin: 14px auto 0; }
  .outline-btn { position: absolute; border: 1px solid #999; background: transparent; font-size: 11.5px; color: #555;
    display: flex; align-items: center; justify-content: center; font-family: "Open Sans", Arial, sans-serif; }

  /* News */
  .news-card { position: absolute; top: 1917px; width: 297px; height: 144px; border: 1px solid var(--line);
    padding: 18px 19px; font-family: "Open Sans", Arial, sans-serif; }
  .news-card h4 { font-size: 16.5px; font-weight: 400; color: #222; }
  .news-card time { display: block; font-size: 11px; color: #555; margin-top: 9px; }
  .news-card p { font-size: 10.8px; line-height: 18px; color: #444; margin-top: 8px; height: 54px; overflow: hidden; }

  /* Contact band & footer */
  .contact-band { position: absolute; left: 0; top: 2199px; width: 1200px; height: 97px; background: var(--band);
    display: flex; align-items: center; justify-content: center; gap: 16px; font-size: 21px; color: #555; }
  .contact-band span { display: inline-flex; align-items: center; gap: 8px; }
  .site-footer { position: absolute; left: 0; top: 2296px; width: 1200px; height: 163px; background: var(--footer); text-align: center; }
  .footer-nav { margin-top: 40px; font-size: 11.5px; color: #333; }
  .footer-nav a { color: #333; text-decoration: none; margin: 0 7px; }
  .copyright { margin-top: 11px; font-size: 11px; color: #444; }
  .social { display: flex; justify-content: center; gap: 24px; margin-top: 22px; }
  .social span { width: 18px; height: 18px; border-radius: 50%; border: 2px solid var(--icon); }
</style>
</head>
<body>

<header class="hero">
  <div class="hero-photo" role="img" aria-label="Bright kitchen with speckled granite worktops, white cabinets, steel appliances and a dark wood floor"></div>
  <div class="brand-box">
    <span class="brand-dot"></span>
    <span class="brand-name">Brightfold Panes &amp; Worktops</span>
  </div>
  <nav class="main-nav">
    <a>Home</a><a>Projects</a><a>News</a><a>Team</a><a>About us</a><a>Contact us</a>
  </nav>
  <h1 class="hero-title">Curabitur venenatis cursus<br>lacinia ornare</h1>
  <a class="hero-btn">Contact Us</a>
  <svg class="hero-arrow" style="left:52px" width="20" height="20" viewBox="0 0 20 20"><path d="M13 3 L6 10 L13 17" fill="none" stroke="#fff" stroke-width="3"/></svg>
  <svg class="hero-arrow" style="left:1128px" width="20" height="20" viewBox="0 0 20 20"><path d="M7 3 L14 10 L7 17" fill="none" stroke="#fff" stroke-width="3"/></svg>
</header>

<section class="welcome">
  <h2 class="welcome-title">Welcome</h2>
  <p class="welcome-text">Nullam lorem urna, tempus eget mollis et, dapibus ac sem. Suspendisse gravida ornare erat sed pulvinar.<br>Vestibulum luctus ex in egestas fringilla. Fusce nec leo ac urna pulvinar auctor. Mauris bibendum fringilla velit.<br>Nulla in lorem at massa pellentesque posuere. Nulla tristique posuere molestie. Aliquam erat volutpat. Etiam<br>quis aliquet risus. Duis ornare erat eget magna dapibus, in accumsan quam pharetra. Nam tempus, quam in<br>bibendum vulputate, sapien dolor viverra nisl, vitae euismod elit turpis et nulla. Aliquam erat volutpat.<br>Pellentesque blandit lacus eget nunc faucibus, et tincidunt eros viverra. Phasellus consequat sagittis nisi<br>suscipit feugiat. Cras eget leo sed nunc hendrerit ultricies eu at nisl. Praesent iaculis faucibus urna sit amet<br>lacinia. Maecenas consequat justo enim, ac mattis massa imperdiet quis. Fusce eget neque elit. Sed augue<br>orci, elementum in magna congue, tincidunt vulputate erat. Aliquam consectetur orci molestie dictum<br>molestie. Proin eget congue nulla, vel tempor diam</p>
  <div class="welcome-media" role="img" aria-label="Close-up of stacked green-tinted glass sheets"></div>
</section>

<section class="projects">
  <h2 class="section-title" style="top:1102px">Latest Projects</h2>
  <svg class="slider-btn" style="left:133px" viewBox="0 0 22 22"><path d="M13 6 L8 11 L13 16" fill="none" stroke="#666" stroke-width="1.5"/></svg>
  <svg class="slider-btn" style="left:1045px" viewBox="0 0 22 22"><path d="M9 6 L14 11 L9 16" fill="none" stroke="#666" stroke-width="1.5"/></svg>

  <div class="project-tile" style="left:0;top:1164px;height:315px;background:linear-gradient(90deg,#8e8289 0%,#b9aeb0 35%,#d6cfcd 55%,#e6d94a 75%,#dcc83a 100%)" role="img" aria-label="Gloved hand cleaning a glass shelf"></div>
  <div class="project-tile" style="left:400px;top:1177px;height:302px;background:linear-gradient(180deg,#f1f0ee 0%,#e9e7e3 36%,#6d655e 44%,#4d4640 100%)" role="img" aria-label="Solid surface worktop over a dark wood cabinet"></div>
  <div class="project-tile" style="left:800px;top:1177px;height:302px;background:linear-gradient(180deg,#ecebe8 0%,#dcd8d2 45%,#f4f3f1 68%,#a8998a 100%)" role="img" aria-label="Modern white kitchen with an integrated sink"></div>
  <div class="project-tile" style="left:0;top:1479px;height:303px;background:linear-gradient(90deg,#d9ab4a 0%,#9cc7bc 30%,#cfe6e0 60%,#7fb6a8 100%)" role="img" aria-label="Stack of clear glass panes"></div>
  <div class="project-card">
    <h3>Fusce sollicitudin luctus</h3>
    <p>Aenean facilisis tincidunt lectus, id dictum nisi luctus eget. Vivamus efficitur ex condimentum, malesuada eros eget, feugiat nibh. Sed tellus ex, imperdiet eget gravida sit amet, volutpat eget turpis. In nec ultricies est. Etiam mattis augue vehicula odio posuere, sit amet tempus lectus.</p>
    <a class="outline-btn" style="left:148px;top:206px;width:103px;height:43px">Read More</a>
  </div>
  <div class="project-tile" style="left:800px;top:1479px;height:303px;background:linear-gradient(180deg,#f0f0f0 0%,#d6d8d9 45%,#a3a6a8 75%,#6f7174 100%)" role="img" aria-label="Glass office desk with a chair by a bright window"></div>
</section>

<section class="news">
  <h2 class="section-title" style="top:1851px">News</h2>
  <article class="news-card" style="left:133px">
    <h4>Fusce sollicitudin lorem et luctus</h4>
    <time>6 August, 2018</time>
    <p>Possibilité de typer les champs personnalisés, refonte du moteur de recherche d'événements et amélioration des performances de l'application</p>
  </article>
  <article class="news-card" style="left:452px">
    <h4>In tristique tristique nulla</h4>
    <time>6 August, 2018</time>
    <p>Création de plusieurs plannings par ressource, superposition d'événements à la même heure, nouveau module de suivi des heures travaillées et</p>
  </article>
  <article class="news-card" style="left:771px">
    <h4>Maecenas vel tortor accumsan</h4>
    <time>6 August, 2018</time>
    <p>Création d'événements de moins de 15 minutes et multi-participants, refonte du moteur de recherche de ressources, amélioration du pack mobilité.</p>
  </article>
  <a class="outline-btn" style="left:552px;top:2083px;width:97px;height:37px">VIEW ALL</a>
</section>

<div class="contact-band">
  <span>
    <svg width="16" height="16" viewBox="0 0 24 24"><path d="M6.6 10.8c1.4 2.8 3.8 5.1 6.6 6.6l2.2-2.2c.3-.3.7-.4 1-.2 1.1.4 2.3.6 3.6.6.6 0 1 .4 1 1V20c0 .6-.4 1-1 1C10.6 21 3 13.4 3 4c0-.6.4-1 1-1h3.5c.6 0 1 .4 1 1 0 1.3.2 2.5.6 3.6.1.3 0 .7-.2 1z" fill="#555"/></svg>
    Phone : 456 555 0148
  </span>
  <span>/</span>
  <span>
    <svg width="18" height="14" viewBox="0 0 24 18"><rect x="0" y="0" width="24" height="18" rx="2" fill="#555"/><path d="M1 2 L12 10 L23 2" fill="none" stroke="#ececec" stroke-width="2"/></svg>
    Eamil : info@brightfoldpw.com
  </span>
</div>

<footer class="site-footer">
  <nav class="footer-nav">
    <a>Home</a>|<a>Projects</a>|<a>News</a>|<a>Team</a>|<a>About us</a>|<a>Contact us</a>
  </nav>
  <p class="copyright">Copyright &copy; 2018 Brightfold Panes and Worktops. &nbsp;All rights reserved.</p>
  <div class="social">
    <span aria-label="Social link"></span><span aria-label="Social link"></span><span aria-label="Social link"></span>
  </div>
</footer>

</body>
</html>
```